July 4th Postcard to existing clients

5x7 postcard wishing our clients happy 4th of July. Card should read on the back "Thank You For Being A Valued Client!. Stay Safe And Enjoy Your Independence Day Celebrations!"

Patriotic theme with fireworks is ideal. We are a law firm so should still have a feel of professionalism while still being fun since it is for a fun holiday.

```html
<!DOCTYPE html>
<html lang="en">
<head>
<meta charset="utf-8">
<title>Independence Day Client Postcard</title>
<link rel="stylesheet" href="https://fonts.googleapis.com/css2?family=Archivo+Black&family=Great+Vibes&family=Allura&family=Open+Sans:wght@400;600&display=swap">
<style>
  :root {
    --canvas-bg: #f2f0ec;
    --sky-blue: #8fa9d4;
    --denim: #6f8fc4;
    --flag-red: #b8283a;
    --flag-white: #f4f1ee;
    --card-back: #ececec;
    --ink: #1d1d1d;
    --logo-ink: #4a4f5a;
    --rule: #c9c9c9;
  }
  * { box-sizing: border-box; margin: 0; padding: 0; }
  html, body { width: 1200px; height: 1200px; overflow: hidden; }
  body {
    background: var(--canvas-bg);
    position: relative;
    font-family: "Open Sans", sans-serif;
  }
  .postcard {
    position: absolute;
    top: 222px;
    width: 540px;
    height: 756px;
    overflow: hidden;
    box-shadow: 0 6px 22px rgba(0,0,0,0.18);
  }
  .postcard--front { left: 40px; }
  .postcard--back { left: 620px; background: var(--card-back); }

  /* front */
  .front-photo {
    position: absolute; inset: 0;
    background:
      radial-gradient(ellipse 30% 18% at 25% 30%, rgba(255,200,120,0.7), transparent 70%),
      linear-gradient(90deg, transparent 18%, rgba(184,40,58,0.55) 22%, rgba(244,241,238,0.5) 32%, rgba(184,40,58,0.45) 40%, transparent 48%),
      linear-gradient(160deg, var(--sky-blue) 0%, var(--denim) 60%, #5a6f99 100%);
  }
  .brand-tag {
    position: absolute;
    left: 275px; top: 19px;
    width: 244px; height: 105px;
    background: rgba(235,238,245,0.55);
    display: flex; flex-direction: column;
    align-items: center; justify-content: flex-end;
    gap: 12px;
    padding-bottom: 14px;
  }
  .brand-tag__square {
    width: 16px; height: 16px;
    background: var(--logo-ink);
  }
  .brand-tag__name {
    font-family: "Open Sans", sans-serif;
    font-weight: 400;
    font-size: 22px;
    line-height: 1;
    letter-spacing: 1px;
    white-space: nowrap;
    color: var(--logo-ink);
  }
  .greeting {
    position: absolute;
    left: 0; right: 0; top: 340px;
    text-align: center;
    font-family: "Great Vibes", cursive;
    font-size: 62px;
    line-height: 1;
    white-space: nowrap;
    color: var(--flag-white);
  }
  .headline {
    position: absolute;
    left: 0; right: 0; top: 482px;
    text-align: center;
    font-family: "Archivo Black", sans-serif;
    font-size: 196px;
    line-height: 0.78;
    letter-spacing: -5px;
    white-space: nowrap;
    color: var(--flag-white);
    opacity: 0.92;
    transform: scaleY(1.45);
    transform-origin: top center;
  }

  /* back */
  .back-photo {
    position: absolute;
    left: 60px; top: 100px;
    width: 380px; height: 656px;
    background: radial-gradient(ellipse 50% 45% at 50% 45%, rgba(120,90,60,0.22), rgba(120,90,60,0.05) 70%, transparent 100%);
  }
  .stamp-box {
    position: absolute;
    left: 387px; top: 31px;
    width: 104px; height: 141px;
    border: 2px solid #b7b7b7;
  }
  .address-line {
    position: absolute;
    left: 50px; width: 445px;
    border-top: 1px solid var(--rule);
  }
  .address-line--1 { top: 246px; }
  .address-line--2 { top: 298px; }
  .address-line--3 { top: 351px; }
  .thanks {
    position: absolute;
    left: 0; right: 0; top: 440px;
    text-align: center;
    font-family: "Allura", cursive;
    font-size: 58px;
    line-height: 1.1;
    color: var(--ink);
  }
  .wishes {
    position: absolute;
    left: 40px; right: 40px; top: 622px;
    text-align: center;
    font-size: 18px;
    line-height: 1.25;
    color: var(--ink);
  }
</style>
</head>
<body>
  <section class="postcard postcard--front">
    <div class="front-photo" role="img" aria-label="Photo of a person in a denim shirt with an American flag, holding lit sparklers"></div>
    <div class="brand-tag">
      <span class="brand-tag__square"></span>
      <span class="brand-tag__name">HALVORSEN LEGAL</span>
    </div>
    <p class="greeting">Happy 4th of July</p>
    <p class="headline">USA</p>
  </section>

  <section class="postcard postcard--back">
    <div class="back-photo" role="img" aria-label="Faint photo of a wooden judge's gavel"></div>
    <div class="stamp-box"></div>
    <div class="address-line address-line--1"></div>
    <div class="address-line address-line--2"></div>
    <div class="address-line address-line--3"></div>
    <p class="thanks">Thank You For Being A<br>Valued Client!</p>
    <p class="wishes">Stay Safe And Enjoy Your Independence Day<br>Celebrations!</p>
  </section>
</body>
</html>
```